Business card design for a dynamic IT consulting company

We need a business card design for a young firm, specialized in the Telecommunications/Consulting industry. The name of the company is Brask and Partners Business Consulting Ltd. (Short name: Brask and Partnes)
Brask = solve read reverse, so we aim to be uncomplicated and solution-oriented. The small pipe in our logo is also related to the word solve. So we need a new business card design, which is simple, eye catching and something non traditional (I would probably prefer a square shaped design rather than a rectangle, but open for suggestions). Attached our logo.

Target Market(s)

Usually our customers are Tier1 Telecoms providers (Q-Linkra, Parnexo, etc) and their executives.

Industry/Entity Type

Business

Contact Information for Business Card

Name: Gergely Halmindo
Email: g.halmindo@braskpartnera.hu
Web: www.braskpartnera.hu
Mobile: +36 30 555 0192
Title: Managing Director

Optional:
Company name: Brask and Partners Ltd.
Address: 1047 Budapest, Ravaszi str. 17/B, Hungary

Font styles to use
Other font styles liked:
• helveticaneue_medium, Prime Regular are used now.

Colors

Designer to choose colors to be used in the design.

Requirements
Must have
• I would like to have a 2 sided design.
Nice to have
• I thought if we make the logo a bit bigger (without the company name), that could go to the back with the company name below. I though, if the pipe in the logo is somehow touchable on the business card, would be nice and unique.

```html
<!DOCTYPE html>
<html lang="en">
<head>
<meta charset="utf-8">
<title>Brask and Partners – Business Card</title>
<link rel="stylesheet" href="https://fonts.googleapis.com/css2?family=Electrolize&display=swap">
<style>
  :root {
    --stage: #141414;
    --card: #0a0a0a;
    --card-edge: #1c1c1c;
    --ink: #f2f2f2;
    --accent-blue: #1e9ad6;
    --accent-pink: #c0399a;
    --muted: #8a8a8a;
  }
  * { margin: 0; padding: 0; box-sizing: border-box; }
  html, body {
    width: 1200px; height: 900px; overflow: hidden;
    background: var(--stage);
    font-family: "Electrolize", "Segoe UI", sans-serif;
    color: var(--ink);
  }
  .stage { position: relative; width: 1200px; height: 900px; }

  .card {
    position: absolute;
    width: 520px; height: 297px;
    background: linear-gradient(160deg, #121212 0%, var(--card) 60%);
    border: 1px solid var(--card-edge);
    border-radius: 4px;
    box-shadow: 0 18px 40px rgba(0,0,0,.6);
    overflow: hidden;
  }
  .card--contact { left: 60px; top: 470px; }
  .card--brand { left: 620px; top: 150px; }

  /* contact side */
  .brand-block {
    position: absolute; left: 34px; top: 70px;
    display: flex; align-items: center; gap: 10px;
  }
  .brand-block__square { width: 16px; height: 16px; background: var(--accent-blue); }
  .brand-block__name { font-size: 26px; color: var(--ink); letter-spacing: .5px; }

  .divider {
    position: absolute; left: 178px; top: 58px;
    width: 2px; height: 150px; background: var(--ink);
  }
  .details { position: absolute; left: 198px; top: 62px; }
  .details__name { font-size: 22px; letter-spacing: 1px; text-transform: uppercase; }
  .details__title { font-size: 15px; color: var(--accent-blue); margin-top: 2px; }
  .details__list { list-style: none; margin-top: 16px; }
  .details__item { display: flex; align-items: center; gap: 9px; font-size: 14px; margin-bottom: 7px; }
  .details__icon { width: 16px; height: 16px; flex: none; }

  .square-field {
    position: absolute; right: 0; top: 0;
    width: 200px; height: 297px;
    background: linear-gradient(90deg, rgba(255,255,255,0) 0%, rgba(255,255,255,.05) 100%);
  }
  .square-field--bright {
    width: 220px;
    background: linear-gradient(90deg, rgba(255,255,255,0) 0%, rgba(200,200,200,.18) 60%, rgba(255,255,255,.35) 100%);
  }

  /* brand side */
  .brand-side {
    position: absolute; left: 48px; top: 120px;
    display: flex; align-items: center; gap: 12px;
  }
  .brand-side__square { width: 18px; height: 18px; background: var(--accent-pink); }
  .brand-side__name { font-size: 34px; color: var(--ink); }
</style>
</head>
<body>
<main class="stage">

  <section class="card card--brand" aria-label="Card back">
    <div class="brand-side">
      <span class="brand-side__square"></span>
      <span class="brand-side__name">Brask &amp; Partners</span>
    </div>
    <div class="square-field square-field--bright" role="img" aria-label="Field of silver squares fading in from the right edge"></div>
  </section>

  <section class="card card--contact" aria-label="Card front">
    <div class="brand-block">
      <span class="brand-block__square"></span>
      <span class="brand-block__name">Brask</span>
    </div>
    <div class="divider"></div>
    <div class="details">
      <p class="details__name">Gergely Halmindo</p>
      <p class="details__title">Managing Director</p>
      <ul class="details__list">
        <li class="details__item">
          <svg class="details__icon" viewBox="0 0 16 16"><rect width="16" height="16" fill="var(--accent-blue)"/><path d="M5 3h2l1 3-1.5 1a6 6 0 0 0 2.5 2.5L10 8l3 1v2a2 2 0 0 1-2 2A9 9 0 0 1 3 5a2 2 0 0 1 2-2z" fill="#fff"/></svg>
          +36 30 555 0192
        </li>
        <li class="details__item">
          <svg class="details__icon" viewBox="0 0 16 16"><rect width="16" height="16" fill="var(--accent-blue)"/><rect x="3" y="4.5" width="10" height="7" fill="none" stroke="#fff"/><path d="M3 4.5l5 4 5-4" fill="none" stroke="#fff"/></svg>
          g.halmindo@braskpartnera.hu
        </li>
        <li class="details__item">
          <svg class="details__icon" viewBox="0 0 16 16"><rect width="16" height="16" fill="var(--accent-blue)"/><circle cx="8" cy="8" r="5" fill="none" stroke="#fff"/><path d="M3 8h10M8 3c-2 2.5-2 7.5 0 10M8 3c2 2.5 2 7.5 0 10" fill="none" stroke="#fff"/></svg>
          www.braskpartnera.hu
        </li>
      </ul>
    </div>
    <div class="square-field" role="img" aria-label="Faint field of dark grey squares"></div>
  </section>

</main>
</body>
</html>
```